Business Bench-marking brochure

Create a single page flyer for an account firm to advertise their Business Bench-marking product offering.

Style should follow new corporate image in development as per attached website psd.

The client likes the logo to always be on the RIGHT of publications.

Target Market(s)

Small - Medium sucessfully Business

Industry/Entity Type

Business

Colors
eb1f27

Requirements
Nice to have
• The client would like an image of a scales with Apples on both sides to be used -the idea being "comparing apples to apples"

```html
<!DOCTYPE html>
<html lang="en">
<head>
<meta charset="utf-8">
<title>Business Benchmarking – Harbor Business Consulting</title>
<link rel="stylesheet" href="https://fonts.googleapis.com/css2?family=Open+Sans:ital,wght@0,400;0,600;0,700;0,800;1,700;1,800&family=Oswald:wght@500;600&display=swap">
<style>
  :root {
    --red: #eb1f27;
    --charcoal: #2f2f2f;
    --slate: #4a4a4a;
    --text-grey: #5b5b5b;
    --panel: #ffffff;
    --apple-red: #c8242a;
    --apple-green: #9fb03a;
  }
  * { margin: 0; padding: 0; box-sizing: border-box; }
  html, body { width: 872px; height: 1200px; overflow: hidden; }
  body {
    font-family: "Open Sans", Arial, sans-serif;
    background: radial-gradient(ellipse 75% 40% at 50% 22%, #f4f4f4 0%, #d6d6d6 45%, #6a6a6a 80%, #2c2c2c 100%);
    background-color: #2c2c2c;
    position: relative;
  }
  .flyer { position: absolute; inset: 0; }

  .headline {
    position: absolute; left: 0; right: 0; top: 18px;
    text-align: center; color: var(--red);
    font-weight: 800; font-style: italic; font-size: 45px; letter-spacing: -0.5px;
  }
  .subhead {
    position: absolute; left: 0; right: 0; top: 80px;
    text-align: center; color: var(--slate);
    font-weight: 400; font-size: 29px;
  }
  .question {
    position: absolute; left: 150px; top: 128px; z-index: 2;
  }
  .question .lead { display: block; color: var(--slate); font-size: 33px; font-weight: 400; }
  .question .key {
    display: inline-block; margin-top: 2px; padding: 0 14px 4px 6px;
    background: var(--panel); color: var(--red);
    font-size: 52px; font-weight: 700; line-height: 1.1;
  }

  .hero-photo {
    position: absolute; left: 60px; top: 170px; width: 752px; height: 380px;
    background: radial-gradient(ellipse 40% 48% at 62% 40%, var(--apple-red) 0%, #a01c22 40%, transparent 62%),
                linear-gradient(180deg, #e9e9e9 0%, #ffffff 60%, #dcdcdc 100%);
    border-radius: 4px;
  }

  .content {
    position: absolute; left: 43px; right: 43px; top: 555px; height: 610px;
    background: var(--panel);
    padding: 12px 40px 0;
    color: var(--text-grey);
  }
  .intro { font-size: 22px; font-weight: 400; line-height: 1.3; }
  .intro-why { font-size: 20px; margin-top: 10px; line-height: 1.3; }
  .body-copy { margin: 20px 60px 0 75px; font-size: 12.5px; line-height: 1.45; color: #444; }
  .body-copy p { margin-bottom: 9px; }
  .body-copy ol { margin: 0 0 9px 22px; }

  .footer {
    position: absolute; left: 0; right: 0; top: 440px;
    display: flex; align-items: center; justify-content: space-between;
    padding: 0 30px 0 10px;
  }
  .brand { display: flex; align-items: center; gap: 14px; }
  .brand-mark { width: 34px; height: 34px; background: var(--red); }
  .brand-name {
    font-family: "Oswald", Arial, sans-serif; font-weight: 600;
    color: var(--charcoal); font-size: 46px; line-height: 1;
    text-transform: uppercase;
  }
  .brand-name small { display: block; font-size: 20px; letter-spacing: 2px; margin-top: 4px; }
  .contact { color: var(--slate); font-size: 26px; line-height: 1.35; }
  .contact .email { font-size: 24px; }
</style>
</head>
<body>
<main class="flyer">
  <h1 class="headline">Does your business stack up?</h1>
  <p class="subhead">Help your business operate at its peak performance</p>
  <h2 class="question"><span class="lead">How do you</span><span class="key">measure up?</span></h2>

  <div class="hero-photo" role="img" aria-label="Photo of a red apple sitting on a white weighing scale wrapped with a yellow tape measure"></div>

  <section class="content">
    <p class="intro">Ever wondered how your business compares to your competitors?</p>
    <p class="intro intro-why">Why you may be struggling to make a profit while other businesses in your industry seem to have it all figured out?</p>

    <div class="body-copy">
      <p>By capturing the financial information and KPIs of your business we can compare your business to those within your industry. This enables you to be armed with the knowledge of how you can take corrective action by making informed decisions to save money and significantly enhance your overall performance. Benchmarking helps you:</p>
      <ol>
        <li>Identify where you can reduce costs and improve efficiencies</li>
        <li>Determine the productivity of your employees</li>
        <li>Highlight opportunities for improvement and innovative practices</li>
        <li>Discover opportunities for making business more competitive</li>
      </ol>
      <p>To ensure your business is operating at its peak performance call Harbor Business Consulting for your detailed benchmark report.</p>
      <p>Full analysis of your financial statements, including KPIs, along with a meeting with Joanna Reeve to identify areas to improve to help your business prosper.</p>
    </div>

    <div class="footer">
      <div class="brand">
        <div class="brand-name">Harbor<small>Business Consulting</small></div>
        <span class="brand-mark" aria-hidden="true"></span>
      </div>
      <div class="contact">
        <p>Contact us : 02 5550 1842</p>
        <p class="email">admin@harborconsulting.com.au</p>
      </div>
    </div>
  </section>
</main>
</body>
</html>
```